A Speech Therapy Business needs to update their logo

I need an update to the font and color of my logo to look more appealing. I am looking to open a private practice as a Speech Language Pathologist that caters to adults and children. It needs to be sophisticated and friendly at the same time. I want to keep the silhouette in my logo as is, just update the font and color for "Brightpaths".
Industry/Entity Type
Business
Contact Information for Business Card
I want the business card to have my logo, my name (Dorota Valk, CCC-SLP, TSSLD) and that I am a Bilingual Speech Language Pathologist. Also, include my phone number, (555) 271-8390. Include my website, Brightpathsslp.example, and email address, dorotavalk@brightpathsslp.example
Look and feel
Each slider illustrates characteristics of the customer's brand and the style your logo design should communicate.

```html
<!DOCTYPE html>
<html lang="en">
<head>
<meta charset="utf-8">
<title>Brightpaths business card</title>
<link rel="stylesheet" href="https://fonts.googleapis.com/css2?family=Open+Sans:wght@400;600;700;800&display=swap">
<style>
  :root {
    --page-bg: #d9dadb;
    --teal: #0f5574;
    --cream: #efebdf;
    --ink-navy: #0f4f72;
    --ink-grey: #5a5a58;
    --taupe: #8f8478;
    --white: #f4f2ec;
  }
  * { box-sizing: border-box; margin: 0; padding: 0; }
  html, body { width: 1200px; height: 786px; overflow: hidden; }
  body {
    background: var(--page-bg);
    font-family: "Open Sans", sans-serif;
    display: flex;
    align-items: center;
    justify-content: center;
    gap: 48px;
  }
  .card {
    width: 525px;
    height: 300px;
    border-radius: 18px;
    position: relative;
    overflow: hidden;
    box-shadow: 0 6px 18px rgba(0,0,0,0.18);
  }
  .card-front { background: var(--cream); }
  .card-back { background: var(--teal); display: flex; flex-direction: column; align-items: center; justify-content: center; }

  .contact { position: absolute; left: 34px; top: 40px; width: 222px; color: var(--ink-grey); }
  .contact-name { font-size: 18px; font-weight: 700; color: var(--ink-navy); letter-spacing: 0.3px; white-space: nowrap; }
  .contact-name .credentials { font-size: 11.5px; font-weight: 400; color: var(--ink-grey); letter-spacing: 0; }
  .contact-title { font-size: 12.5px; line-height: 1.35; margin-top: 4px; max-width: 180px; }
  .contact-list { list-style: none; margin-top: 16px; font-size: 11.5px; line-height: 1.75; }
  .contact-list li { display: flex; align-items: center; gap: 7px; white-space: nowrap; }
  .contact-list svg { width: 11px; height: 11px; flex: none; }

  .divider { position: absolute; left: 270px; top: 40px; bottom: 40px; width: 1px; background: rgba(143,132,120,0.3); }

  .wordmark { display: flex; align-items: center; gap: 8px; font-weight: 800; text-transform: uppercase; letter-spacing: 0.5px; white-space: nowrap; }
  .wordmark .mark-dot { border-radius: 50%; background: var(--taupe); flex: none; }
  .card-front .wordmark { position: absolute; left: 294px; top: 158px; font-size: 24px; color: var(--ink-navy); }
  .card-front .mark-dot { width: 13px; height: 13px; }
  .card-back .wordmark { font-size: 34px; color: var(--white); }
  .card-back .mark-dot { width: 18px; height: 18px; }
  .web { margin-top: 14px; font-size: 13px; color: var(--white); letter-spacing: 0.3px; }
</style>
</head>
<body>
  <section class="card card-front" aria-label="Card front">
    <div class="contact">
      <p class="contact-name">DOROTA VALK, <span class="credentials">CCC-SLP, TSSLD</span></p>
      <p class="contact-title">Bilingual Speech Language Pathologist</p>
      <ul class="contact-list">
        <li><svg viewBox="0 0 12 12" aria-hidden="true"><path d="M2.5 1 L4.5 1 L5.2 3.4 L4 4.3 Q5 6.8 7.7 8 L8.6 6.8 L11 7.5 L11 9.5 Q10.5 11 9 11 Q1 10 1 2.5 Q1 1.2 2.5 1Z" fill="var(--ink-navy)"/></svg>(555) 271-8390</li>
        <li><svg viewBox="0 0 12 12" aria-hidden="true"><rect x="0.5" y="2.5" width="11" height="7" fill="var(--ink-navy)"/><path d="M0.5 2.5 L6 6.5 L11.5 2.5" stroke="var(--cream)" fill="none"/></svg>dorotavalk@brightpathsslp.example</li>
        <li><svg viewBox="0 0 12 12" aria-hidden="true"><circle cx="6" cy="6" r="5.3" fill="var(--ink-navy)"/><path d="M0.8 6 H11.2 M6 0.7 V11.3 M6 0.7 Q2.5 6 6 11.3 M6 0.7 Q9.5 6 6 11.3" stroke="var(--cream)" stroke-width="0.8" fill="none"/></svg>www.brightpathsslp.example</li>
      </ul>
    </div>
    <div class="divider"></div>
    <div class="wordmark"><span class="mark-dot"></span>Brightpaths</div>
  </section>

  <section class="card card-back" aria-label="Card back">
    <div class="wordmark"><span class="mark-dot"></span>Brightpaths</div>
    <p class="web">www.brightpathsslp.example</p>
  </section>
</body>
</html>
```